VELORIAIR Business Card

We need a new elegant business card.
We are a company of business jet.
In attachment the old business card (2 sides) and the new logo.

Our adress is :
Aérodrome de Marvenne le Clos - Bât.207
78204 MARVENNE LE CLOS - FRANCE

Target Market(s)

Lux

Industry/Entity Type

Business

Contact Information for Business Card

You can see the example in attachment

Font styles to use
Serif
Sans Serif

Requirements
Must have
• The color of the logo (white, black, blue)

```html
<!DOCTYPE html>
<html lang="fr">
<head>
<meta charset="utf-8">
<title>VELORIAIR Business Card</title>
<link rel="stylesheet" href="https://fonts.googleapis.com/css2?family=Raleway:wght@400;500;700&display=swap">
<style>
  :root {
    --backdrop: #e9e7e3;
    --card-white: #ffffff;
    --card-black: #000000;
    --ink: #1d1d1f;
    --ink-soft: #3a3a3c;
    --brand-blue: #1fb0e6;
  }
  * { box-sizing: border-box; margin: 0; padding: 0; }
  html, body {
    width: 1200px;
    height: 800px;
    overflow: hidden;
    background: var(--backdrop);
    font-family: "Raleway", "Helvetica Neue", Arial, sans-serif;
  }
  .canvas {
    width: 1200px;
    height: 800px;
    display: flex;
    align-items: center;
    justify-content: center;
    gap: 60px;
  }
  .card {
    width: 525px;
    height: 300px;
    border-radius: 3px;
    box-shadow: 0 10px 30px rgba(0,0,0,0.18), 0 2px 6px rgba(0,0,0,0.12);
    position: relative;
  }
  .card--front {
    background: var(--card-white);
    color: var(--ink);
    padding: 30px 34px;
  }
  .card--back {
    background: var(--card-black);
    display: flex;
    align-items: center;
    justify-content: center;
  }
  .brand {
    display: flex;
    align-items: center;
    gap: 8px;
    font-weight: 700;
    letter-spacing: 0.06em;
    color: var(--ink);
  }
  .brand__name { font-size: 26px; line-height: 1; }
  .brand__dot {
    width: 18px; height: 18px;
    border-radius: 50%;
    background: var(--brand-blue);
  }
  .person {
    margin: 18px 0 0 120px;
  }
  .person__name {
    font-size: 24px;
    font-weight: 400;
    line-height: 1.15;
  }
  .person__title {
    font-size: 13px;
    color: var(--brand-blue);
    margin-top: 2px;
  }
  .contact {
    margin: 18px 0 0 120px;
    font-size: 11px;
    line-height: 1.45;
    color: var(--ink-soft);
  }
  .contact__email {
    color: var(--brand-blue);
    margin-top: 10px;
  }
  .address {
    position: absolute;
    left: 154px;
    bottom: 26px;
    font-size: 11px;
    line-height: 1.45;
    color: var(--ink-soft);
  }
  .brand--reverse { gap: 14px; color: var(--card-white); }
  .brand--reverse .brand__name { font-size: 40px; }
  .brand--reverse .brand__dot { width: 26px; height: 26px; }
</style>
</head>
<body>
<main class="canvas">
  <section class="card card--front" aria-label="Recto de la carte">
    <div class="brand">
      <span class="brand__name">VELORIAIR</span>
      <span class="brand__dot"></span>
    </div>
    <div class="person">
      <p class="person__name">Julien Marceau</p>
      <p class="person__title">President/Captain</p>
    </div>
    <div class="contact">
      <p>telephone +33 (0) 1 4728 3190</p>
      <p>fax +33 (0) 1 4728 3191</p>
      <p>mobile +33 (0) 6 5814 2973</p>
      <p class="contact__email">jm@veloriair.com</p>
    </div>
    <address class="address" style="font-style: normal;">
      <p>Aérodrome de Marvenne le Clos - Bât.207</p>
      <p>78204 MARVENNE LE CLOS - FRANCE</p>
    </address>
  </section>

  <section class="card card--back" aria-label="Verso de la carte">
    <div class="brand brand--reverse">
      <span class="brand__name">VELORIAIR</span>
      <span class="brand__dot"></span>
    </div>
  </section>
</main>
</body>
</html>
```